KEB Lau Sound business package.
business cards, stationary, letterhead, envelopes, CD labels and packaging, appointment cards, etc..
Thank you Mr. harven47 !!!!!
CONGRATS 7pixelcrafter
CONGRATS Mr. 7pc!!!!!!!!!!!!!!!!!!
I chose draft #56 as the winner.
I wanted to thank all designers for their great contributions and all your help and great advice.
You guys are all awesome.
I of course wanted to thank Mr. 7pc in particular from the bottom of my heart for always dealing so gracefully and friendly with my sometimes tough to deal with "Mr. Perfectionist" attitude and way of doing things. haha :)
I am super happy with the chosen design.
Fantastic work.
THANK YOU.
Much love to you and your family.
Talor.
@ PH Thank you for your honesty and candor about your likely early decision on the design. I hope all PH's can be as honest and thoughtful. Good luck with your business!!!
It looks like Mr. 7pixelcrafter's draft #48 is going to be the winner.
I know I could always be surprised of course, but I don't think anybody is going to be able to change my mind and beat how I feel about his design.
I know I still have over a day left before this project closes, but... I am only posting this here because I care about your time, talent and energy, and I want to make sure you don't spend extra time and resources on this project if you could be working on other projects where you have a higher likelihood of winning the project.
I am super anxious to see Mr. 7pixelcrafter's revisions I asked for.
My favorite designs btw are:
#20 (all the design AND the business cards), #31 (but not the business cards and not the shirts), #37 and #38
It looks like this is going to go between Mr. 7pixelcrafter and my friend who created the logo Mr. Harven47 for the winning bid.
We seem to have an India vs. India house contest here haha.
At this time: I tend to lean over to really liking #20 and #31 as my favorites.
Tips and pointers:
1) I gravitate towards preferring having the contact info at the bottom of the fax/letterhead (as in #20 and #31)
I have a feeling that the design that is going to win, is going to be the design that has the contact info at the bottom, and the company name more featured on top of the letterhead/fax design.
2) I prefer ligher colors that fit/match as closely as possible to the color of the KEB Lau Sound logo.
3) I tend to prefer having the KEB Lau Sound logo featured.. meaning: larger... on business cards, letterheads, fax pages, actually... everything.
4) I tend to lean towards liking having the big "O" with headphones logo on the lower left corner of fax/letterhead pages as a light background/watermark
5) I REALLY really like it when ALL materials have a certain design element that ties ALL materials together. Which is why I for example REALLY like #20 (ALL the materials have exactly the same design elements
6) I would LOOOOOVEEE to see copies/drafts of my 4 favorite designs mentioned above, with some slight touch of silver added to the white backgrounds of all materials/stationary. (As in the silver-ish kind of background in the original "white/silver background" of the KEB Lau Sound logo file I uploaded for this project)
Fixes:
1) I need to have the 415-738-2261 (cell) number on top of the landline (323 etc) number on all materials. (cell first)
2) I absolutely want the center of the O's in "KEB Lau Sound" to be exactly the same color as the background (on ALL materials). If the background is black, I want the center of the O to be black as well, if it is turquoise, then I want the center of the O to be turquoise as well, etc... etc...
Thank you for all your amazing work.
Much respect and love for all your work and your talent.
Best
First off:
I am SUPER HAPPY with all your submissions. You are ALL doing an amazing job and it is again going to be very hard for me to choose here. :)
So here's some guidance, sharing with you my favorite things I have seen, likes, etc...
Right now my 2 favorite ones are #33 and #31
My favorite color so far is Mr. Harven's #33
Mr Harven, Could I see a copy of the fax sheet and stationary/letterhead with the big O in the lower left corner
1) much lighter in color (kind a like a watermark. My concern is that it might interfere with typed text on the letter as it is now)
2) with that big O moved a bit to the left so the whole symbol is on the page.
3) with the company name/logo bigger on all materials.
(This does not have to be 3 different drafts btw... trying to save you time here... I am looking for one draft that has all these 3 things all together.)
More about #33
I LOVE the simplicity of the footer (bottom of page) you created on the letterhead/footer and fax page.
On the business cards: you did an amazing job on the color of the back of the business card. Keep it that way please haha. However: you know how much I am in love with color of the logo you created: is there any way you can have the logo/business name in the original color (instead of white) on that awesome background you created here?? (not sure if that would work, or if it would be too much of the same color?)
How would it look like if you made the word 'Music" black?
Mr. 7pixelcrafter draft #31
I completely LOVE how you did this smart out of the box thinking thing and made the business cards vertical (which is pretty unusual haha). So cool.
I also really frigging like what you did with the blue hue color lettering in my name and URL on the business cards.
I also adore the design of the fax sheet and letterhead. I really like it's simplicity.
But can I see a draft of the letterhead and fax page: where
1) you make a the company logo top left corner a bit bigger
2) Can you also add the O with head phones in the lower right corner, very lightly (like a watermark type thing)
Lastly: I am trying to figure out how I like the business cards with the company name in the big O.
Part of me is in love with the company logo design, and want to see it bigger and free (meaning: not surrounded by the big O ). I prefer the idea of using that O icon as a lighter background/watermark kind a thing.
Comments for everybody:
1) I need to have my cell phone number and email on the CD labels and on the CD insert sheet.
2) I would like you all to use little icons instead of using the words "cell", "address", "phone", etc...
The reason being that icons are more international: the word "cell" for example in Britain or Australia is confusing, as they call it a "mobile" there.
3) Us a little "house" icon for "address"
4) I want my cell number, to be ABOVE my land line/phone number
5) I want the address LAST. (Think about it: people have short attention spans haha... it's all about marketing and grabbing people... the FIRST thing they want to see is where to get in touch with you right now... your cell phone... not where you live.)
Draft #26 and #27
I like your very smart idea of creating tablature paper, music paper etc... with my logo and business name/logo on. You get extra points sir for that amazing idea. I should have thought of that myself already, but you beat me to it haha.
On the black shirt: I would not put the O logo on the front, as it makes it a bit too heavy and busy, already having my name logo there. I woud make the name logo bigger, and have the big O on the back of the shirt. Also: no tilted O.
On the white top: FANTASTIC artwork with the O logo... I really like the dotted approach you came up with here.
I also like how you picked up on my asking in an earlier post about the more silvery approach I wanted to see examples of.

```html
<!DOCTYPE html>
<html lang="en">
<head>
<meta charset="utf-8">
<title>Mira Vale Music — Stationery Package</title>
<link rel="stylesheet" href="https://fonts.googleapis.com/css2?family=Open+Sans:wght@400;600;700;800&family=Great+Vibes&display=swap">
<style>
  :root{
    --bg:#e6e7e9;
    --paper:#ffffff;
    --silver:#f1f3f5;
    --blue:#2aa3dc;
    --blue-deep:#1577b6;
    --blue-light:#8fd3f2;
    --ink:#333a40;
    --grey:#8a9198;
    --line:#c9cfd4;
    --dark:#3b3f44;
    --darker:#24272b;
  }
  *{box-sizing:border-box;margin:0;padding:0}
  html,body{width:1200px;height:600px;overflow:hidden;background:var(--bg);
    font-family:"Open Sans",Arial,sans-serif;color:var(--ink)}
  .canvas{position:relative;width:1200px;height:600px}
  .sheet{position:absolute;background:var(--paper);box-shadow:0 2px 6px rgba(0,0,0,.18);overflow:hidden}
  .band{position:absolute;left:0;right:0;background:linear-gradient(90deg,var(--blue-deep),var(--blue) 55%,var(--blue-light));}
  .top-band{top:0;height:6px}
  .brand{font-family:"Open Sans",Arial,sans-serif;font-weight:800;color:var(--blue);letter-spacing:-.02em;white-space:nowrap;display:flex;align-items:center;gap:4px}
  .footer{position:absolute;left:0;right:0;bottom:0;height:22px;display:flex;align-items:center;justify-content:center;gap:9px;
    color:#fff;font-size:5px;font-weight:600;white-space:nowrap}
  .footer span{display:flex;align-items:center;gap:2px}
  .footer svg{width:6px;height:6px;fill:#fff}
  .tiny{font-size:5px;line-height:7.2px;color:var(--grey)}

  /* Fax */
  .fax{left:12px;top:24px;width:252px;height:336px}
  .fax-title{position:absolute;left:18px;top:22px;font-size:17px;font-weight:800;color:var(--ink)}
  .fax .brand{position:absolute;right:16px;top:28px;font-size:11px}
  .fax-fields{position:absolute;left:18px;top:62px;width:216px;display:grid;grid-template-columns:1fr 1fr;gap:8px 14px}
  .fax-field{font-size:5.5px;font-weight:600;border-bottom:.6px solid var(--line);padding-bottom:2px;line-height:7px}
  .fax-checks{position:absolute;left:18px;top:138px;width:216px;display:flex;justify-content:space-between;font-size:4.6px;line-height:6px}
  .fax-checks span::before{content:"";display:inline-block;width:4px;height:4px;border:.6px solid var(--ink);margin-right:2px;vertical-align:-1px}
  .fax-rule{position:absolute;left:18px;right:18px;top:152px;height:.8px;background:var(--line)}

  /* Letterhead */
  .letter{left:288px;top:24px;width:252px;height:336px}
  .letter .brand{position:absolute;left:18px;top:24px;font-size:13px}
  .letter-body{position:absolute;left:18px;right:18px;top:60px}
  .letter-body p{margin-bottom:6px}

  /* Invoice */
  .invoice{left:564px;top:24px;width:252px;height:336px}
  .invoice .brand{position:absolute;left:18px;top:22px;font-size:11px}
  .invoice-title{position:absolute;left:0;right:0;top:42px;text-align:center;font-size:11px;font-weight:800;letter-spacing:.08em}
  .invoice-meta{position:absolute;left:18px;top:62px;width:216px;display:flex;justify-content:space-between}
  .invoice-meta .box{width:96px;height:30px;border:.6px solid var(--line)}
  .invoice table{position:absolute;left:18px;top:104px;width:216px;border-collapse:collapse;font-size:4.6px}
  .invoice th{background:var(--silver);font-weight:700;text-align:left;padding:2px;border:.6px solid var(--line)}
  .invoice td{height:9px;border-left:.6px solid var(--line);border-right:.6px solid var(--line)}
  .invoice tr:last-child td{border-bottom:.6px solid var(--line)}
  .invoice-total{position:absolute;right:18px;top:286px;font-size:6px;font-weight:800;border-top:.8px solid var(--ink);padding-top:2px;width:80px;text-align:right}

  /* CD insert & discs */
  .cd-cover{left:836px;top:24px;width:168px;height:178px}
  .cd-cover .brand{position:absolute;left:0;right:0;top:58px;justify-content:center;font-size:16px}
  .cd-cover .band{bottom:0;height:26px}
  .cd-cover .contact{position:absolute;left:14px;bottom:34px;font-size:5px;line-height:7px;color:var(--grey)}
  .disc{position:absolute;border-radius:50%;box-shadow:0 2px 6px rgba(0,0,0,.22);overflow:hidden}
  .disc-light{left:990px;top:24px;width:200px;height:200px;background:var(--paper)}
  .disc-dark{left:840px;top:220px;width:190px;height:190px;background:radial-gradient(circle,var(--dark),var(--darker))}
  .disc .hole{position:absolute;left:50%;top:50%;width:38px;height:38px;margin:-19px 0 0 -19px;border-radius:50%;background:var(--bg);border:6px solid var(--silver)}
  .disc .arc{position:absolute;left:0;right:0;bottom:0;height:34%;background:linear-gradient(90deg,var(--blue-deep),var(--blue))}
  .disc-light .brand{position:absolute;left:0;right:0;top:42px;justify-content:center;font-size:14px}
  .disc-light .contact{position:absolute;left:124px;top:94px;font-size:4.8px;line-height:6.8px;color:var(--grey)}
  .disc-dark .brand{position:absolute;left:0;right:0;top:38px;justify-content:center;font-size:13px;color:var(--blue-light)}

  /* Envelope */
  .envelope{left:12px;top:440px;width:264px;height:134px}
  .envelope .brand{position:absolute;left:14px;top:14px;font-size:11px}
  .envelope .return{position:absolute;left:14px;top:32px}
  .envelope .band{bottom:0;height:14px}

  /* Business cards */
  .card-front{left:318px;top:464px;width:124px;height:92px}
  .card-front .brand{position:absolute;left:10px;top:12px;font-size:8.5px}
  .card-front .person{position:absolute;left:10px;top:34px;font-size:5.5px;font-weight:700;color:var(--blue-deep)}
  .card-front .contact{position:absolute;left:10px;top:43px;font-size:4.4px;line-height:6px;color:var(--grey)}
  .card-front .band{bottom:0;height:9px}
  .card-back{left:468px;top:444px;width:132px;height:106px;background:radial-gradient(circle at 50% 45%,#6b7076,var(--darker))}
  .card-back .brand{position:absolute;left:0;right:0;top:46px;justify-content:center;font-size:10px;color:var(--blue-light)}

  /* Gift certificate */
  .gift{left:732px;top:430px;width:456px;height:150px}
  .gift-photo{position:absolute;left:12px;top:10px;width:118px;height:118px;border-radius:50%;
    background:radial-gradient(circle at 45% 40%,var(--blue-light),var(--blue) 60%,var(--blue-deep))}
  .gift-title{position:absolute;left:150px;top:6px;font-family:"Great Vibes",cursive;font-size:30px;color:var(--blue-deep);white-space:nowrap}
  .gift-sub{position:absolute;left:330px;top:30px;font-size:8px;font-weight:700;color:var(--ink);line-height:10px}
  .gift-body{position:absolute;left:150px;top:52px;width:290px;font-size:5.4px;line-height:8px;color:var(--ink)}
  .gift-body .fill{display:inline-block;width:110px;border-bottom:.6px solid var(--grey)}
  .gift .brand{position:absolute;left:150px;top:112px;font-size:12px}
  .gift .band{bottom:0;height:12px}
  .gift-contact{position:absolute;right:14px;bottom:3px;font-size:4.6px;line-height:6px;color:#fff;font-weight:600}
</style>
</head>
<body>
<svg width="0" height="0" style="position:absolute">
  <symbol id="icon-phone" viewBox="0 0 10 10"><path d="M2 1h2l1 2-1 1c.5 1 1.2 1.8 2 2l1-1 2 1v2c0 .6-.4 1-1 1C4.5 9 1 5.5 1 2c0-.6.4-1 1-1z"/></symbol>
  <symbol id="icon-home" viewBox="0 0 10 10"><path d="M5 1l4 4H8v4H6V6H4v3H2V5H1z"/></symbol>
  <symbol id="icon-mail" viewBox="0 0 10 10"><path d="M1 2h8v6H1zM1.6 2.6 5 5.4l3.4-2.8"/></symbol>
</svg>

<main class="canvas">

  <section class="sheet fax">
    <div class="band top-band"></div>
    <h1 class="fax-title">FAX</h1>
    <div class="brand">Mira Vale Music</div>
    <div class="fax-fields">
      <div class="fax-field">To:</div><div class="fax-field">From:</div>
      <div class="fax-field">Fax:</div><div class="fax-field">Pages:</div>
      <div class="fax-field">Phone:</div><div class="fax-field">Date:</div>
      <div class="fax-field">Re:</div><div class="fax-field">CC:</div>
    </div>
    <div class="fax-checks">
      <span>Urgent</span><span>For Review</span><span>Please Comment</span><span>Please Reply</span><span>Please Recycle</span>
    </div>
    <div class="fax-rule"></div>
    <div class="band footer">
      <span><svg><use href="#icon-phone"/></svg>555-014-2200</span>
      <span><svg><use href="#icon-phone"/></svg>555-019-7731</span>
      <span><svg><use href="#icon-mail"/></svg>hello@miravale.example</span>
      <span><svg><use href="#icon-home"/></svg>Harbor City</span>
    </div>
  </section>

  <section class="sheet letter">
    <div class="band top-band"></div>
    <div class="brand">Mira Vale Music</div>
    <div class="letter-body tiny">
      <p>Dear Client,</p>
      <p>Thank you for choosing our studio for your guitar and music lessons. We are glad to welcome you and look forward to working together on your playing, your sound and your goals over the coming months.</p>
      <p>Each lesson is shaped around your level and the music you love. We cover technique, theory, ear training and songs, so that every session feels useful, relaxed and fun for players of every age and style.</p>
      <p>Your first lesson details are listed below. Please arrive a few minutes early and bring your instrument. If you need to change the time, just call or send a short message and we will gladly find another slot.</p>
      <p>We are happy to have you with us and cannot wait to hear you play.</p>
      <p>Sincerely,<br>Dana</p>
    </div>
    <div class="band footer">
      <span><svg><use href="#icon-phone"/></svg>555-014-2200</span>
      <span><svg><use href="#icon-phone"/></svg>555-019-7731</span>
      <span><svg><use href="#icon-mail"/></svg>hello@miravale.example</span>
      <span><svg><use href="#icon-home"/></svg>Harbor City</span>
    </div>
  </section>

  <section class="sheet invoice">
    <div class="band top-band"></div>
    <div class="brand">Mira Vale Music</div>
    <h2 class="invoice-title">INVOICE</h2>
    <div class="invoice-meta"><div class="box"></div><div class="box"></div></div>
    <table>
      <thead><tr><th>QTY</th><th>DESCRIPTION</th><th>PRICE</th><th>TOTAL</th></tr></thead>
      <tbody>
        <tr><td></td><td></td><td></td><td></td></tr><tr><td></td><td></td><td></td><td></td></tr>
        <tr><td></td><td></td><td></td><td></td></tr><tr><td></td><td></td><td></td><td></td></tr>
        <tr><td></td><td></td><td></td><td></td></tr><tr><td></td><td></td><td></td><td></td></tr>
        <tr><td></td><td></td><td></td><td></td></tr><tr><td></td><td></td><td></td><td></td></tr>
        <tr><td></td><td></td><td></td><td></td></tr><tr><td></td><td></td><td></td><td></td></tr>
        <tr><td></td><td></td><td></td><td></td></tr><tr><td></td><td></td><td></td><td></td></tr>
        <tr><td></td><td></td><td></td><td></td></tr><tr><td></td><td></td><td></td><td></td></tr>
        <tr><td></td><td></td><td></td><td></td></tr><tr><td></td><td></td><td></td><td></td></tr>
      </tbody>
    </table>
    <div class="invoice-total">TOTAL DUE</div>
    <div class="band footer">
      <span><svg><use href="#icon-phone"/></svg>555-014-2200</span>
      <span><svg><use href="#icon-phone"/></svg>555-019-7731</span>
      <span><svg><use href="#icon-home"/></svg>Harbor City</span>
    </div>
  </section>

  <section class="sheet cd-cover">
    <div class="brand">Mira Vale Music</div>
    <div class="contact">Dana<br>555-014-2200<br>hello@miravale.example</div>
    <div class="band"></div>
  </section>

  <section class="disc disc-light">
    <div class="arc"></div>
    <div class="brand">Mira Vale Music</div>
    <div class="contact">Dana<br>555-014-2200<br>hello@miravale.example</div>
    <div class="hole"></div>
  </section>

  <section class="disc disc-dark">
    <div class="arc"></div>
    <div class="brand">Mira Vale Music</div>
    <div class="hole"></div>
  </section>

  <section class="sheet envelope">
    <div class="brand">Mira Vale Music</div>
    <div class="return tiny">555-014-2200<br>555-019-7731<br>Harbor City</div>
    <div class="band"></div>
  </section>

  <section class="sheet card-front">
    <div class="brand">Mira Vale Music</div>
    <div class="person">Dana</div>
    <div class="contact">555-014-2200<br>555-019-7731<br>hello@miravale.example</div>
    <div class="band"></div>
  </section>

  <section class="sheet card-back">
    <div class="brand">Mira Vale Music</div>
  </section>

  <section class="sheet gift">
    <div class="gift-photo" role="img" aria-label="Illustration of a guitarist playing, in blue tones"></div>
    <div class="gift-title">Gift Certificate</div>
    <div class="gift-sub">for<br>Guitar &amp; Music Lessons</div>
    <p class="gift-body">The person who gives you this card cares about you and wants to give you a wonderful gift of music. Enjoy your lessons with one of the best guitar teachers in town.<br>
      To: <span class="fill"></span> From: <span class="fill"></span><br>
      Looking forward to playing with you, Dana</p>
    <div class="brand">Mira Vale Music</div>
    <div class="band"></div>
    <div class="gift-contact">555-014-2200 · hello@miravale.example</div>
  </section>

</main>
</body>
</html>
```